Modern Website For Law Firm Lawyer Melbourne, Australia Coded

We are looking for a modern and sophisticated website design. We would prefer the site to be based on WordPress given it is intuitive and some of our staff have experience using it.

Our law firm is based in Melbourne, Australia and we deal with property. The website must be hosted on a reliable Australian server.

We would also appreciate it if the designer can provide some guidance about how to make changes/upload content, such as photos and articles. We are happy to pay for this advice.

We prefer classic fonts in black or grey. We would also like a dash of colour so please use a green, blue or aqua colour palette that is consistent with our logo attached.

We do not want any law related images - scales of justice, gavel or the like.

Our ultimate goal is to communicate that the firm is professional, affordable, modern, dynamic, knowledgeable and one with the community.

We would like the following pages/sections/icons:

1. Who We Are - we will provide content.

2. Our Services - 1. Property 2. Wills, 3. Powers of Attorney 4. Probate & Estate Administration 5.Consultancy & Agency- we will provide content for each of these sections.

3. Articles - we already have approximately 20 articles on a wordpress blog and would like to port these articles to the website. We can do this ourselves if the designer can give us instructions about how to do this. We would also like to give clients the option to subscribe to our articles.

4. Contact Us - this should include our firms contact details; location map and we would like to give clients the option to "Request A Quote" directly from the page - i.e they will need to provide their full name, phone number email address, choose subject from drop down menu and type a message that gets sent to our outlook email.

5. Terms and Conditions - we will provide content

We really like the style and photographs used in the following website and want something as close to this as possible:

https://www.brelwick.com/

For privacy reasons, we would prefer to provide content together with all business details once we have decided on the winner.

We will monitor entries closely and promise to provide feedback and guidance on each entry.

This project is guaranteed. If our budget is too low please email us so we can discuss further and perhaps increase our budget. We are reasonable in this regard.

Thank you very much for considering this project.

Target Market(s)

General public, professionals, lawyers and conveyancers

Industry/Entity Type

Law Firm

Coding

Coded - Design and coding required

Number of Pages Required

1 page

Font styles to use
Sans Serif

Colors
33b8a4
33a6d7
0692cd
3176b5
00a990
9bcb3c
86cfc6
cadf82
85acd3

Requirements
Must have
• 1. Site must be coded and hosted on a reliable Australian server and it would be much appreciated if the deisgner provides instructions about how to add photos, blog articles etc-
• 2. The site must be secure and have green lock at top of page
• 3. Request A Quote - name, email, phone, drop down subject, message - email to our outlook email
• 4. Article Subscription
• 5. Domain (we have already purchased)
• 6. Location map
• 7. Facebook, LinkedIn, Instagram Icons
• 8. Membership icons in this order - VLQ Member > Coastal Women Advocates > Guide For Counsel > Creature Foundation > Tovra > Parcelnet > Vek QA logos attached to go on bottom of page
• 9. Testimonials
Nice to have
• A modern, sophisticated website like:
• https://www.brelwick.com/ - we really like the style of the brelwick photographs
• We also really like this design by Rk of Sketch swarm:
• https://www.sketchswarm.com.au/design/58201946
Should not have
• Law related images - scales of justice gavel and the like

```html
<!DOCTYPE html>
<html lang="en">
<head>
<meta charset="utf-8">
<title>Ridgeview Lawyers</title>
<link href="https://fonts.googleapis.com/css2?family=Lato:wght@300;400;700&display=swap" rel="stylesheet">
<style>
:root{
  --ink:#2b2b2b;
  --text:#333;
  --muted:#555;
  --line:#d5d5d5;
  --blue:#0692cd;
  --blue-btn:#3a8fd0;
  --green:#13a889;
  --teal:#33b8a4;
  --address:#12a98f;
  --panel:#f3f3f3;
  --white:#fff;
}
*{box-sizing:border-box;margin:0;padding:0}
html,body{width:1200px;height:2456px;overflow:hidden;background:var(--white)}
body{font-family:"Lato",Arial,sans-serif;color:var(--text);position:relative}
.abs{position:absolute}

/* header */
.site-header{left:0;top:0;width:1200px;height:107px;background:var(--white)}
.brand{left:100px;top:20px;display:flex;align-items:center;gap:14px}
.brand-mark{width:62px;height:62px;border-radius:50%;background:var(--teal)}
.brand-name{font-size:24px;font-weight:400;color:#444;line-height:1.05;letter-spacing:.5px}
.brand-name small{display:block;font-size:17px;letter-spacing:1.5px}
.main-nav{left:408px;top:48px;display:flex;gap:34px;font-size:16px;color:#444}
.search-icon{left:1069px;top:50px}

/* hero */
.hero{left:0;top:107px;width:1200px;height:461px;
  background:linear-gradient(180deg,#2d3a57 0%,#3b4560 35%,#4a4550 62%,#5a4030 78%,#27303e 100%)}
.hero-title{left:0;width:1200px;top:158px;text-align:center;color:var(--white);font-size:31px;font-weight:400;letter-spacing:.5px}
.hero-sub{left:400px;width:400px;top:207px;display:flex;align-items:center;gap:14px;color:var(--white);font-size:17px;letter-spacing:1px}
.hero-sub span.rule{flex:1;height:1px;background:#ddd}
.hero-text{left:330px;width:540px;top:233px;text-align:center;color:var(--white);font-size:15.5px;font-weight:700;line-height:27px}
.hero-btn{left:531px;top:301px;width:137px;height:38px;background:var(--blue-btn);color:var(--white);font-size:15px;display:flex;align-items:center;justify-content:center;letter-spacing:.5px}
.hero-arrow{top:212px}

/* intro panels */
.panel{top:520px;height:286px;padding:22px 23px}
.panel-about{left:100px;width:497px;background:var(--panel)}
.panel-news{left:604px;width:496px;background:var(--blue);color:var(--white)}
.panel h2{font-size:22px;font-weight:400;letter-spacing:.5px;margin-bottom:14px}
.panel-about h2{color:var(--ink)}
.panel p{font-size:12.5px;line-height:26px;text-align:justify}
.news-date{font-size:11px;font-weight:700;margin:-8px 0 12px}
.news-headline{font-size:21px;line-height:25px;text-align:justify;margin-bottom:4px}
.outline-btn{display:inline-flex;align-items:center;justify-content:center;height:38px;padding:0 15px;font-size:14px;margin-top:15px}
.panel-about .outline-btn{border:1px solid var(--blue-btn);color:#2f5f9a;background:var(--white)}
.panel-news .outline-btn{border:1px solid var(--white);color:var(--white);margin-top:10px}

/* features */
.features-title{left:0;width:1200px;top:887px;text-align:center;font-size:20px;font-weight:300;color:#222;line-height:24px;letter-spacing:.3px}
.features-intro{left:200px;width:800px;top:964px;text-align:center;font-size:12.5px;line-height:26px;color:var(--text)}
.feature{top:1068px;width:280px;text-align:center}
.feature h3{font-size:23px;font-weight:400;color:#222;margin-bottom:14px}
.feature p{font-size:12px;line-height:26px;padding:0 8px}
.small-btn{display:inline-flex;align-items:center;gap:8px;height:32px;padding:0 12px;border:1px solid #8aa7c8;font-size:13px;color:#333;margin-top:18px}
.tri{width:0;height:0;border-left:6px solid var(--green);border-top:4px solid transparent;border-bottom:4px solid transparent}

/* articles */
.articles-title{left:0;width:1200px;top:1305px;text-align:center;font-size:20px;font-weight:300;color:#222;letter-spacing:.5px}
.card{top:1374px;width:302px;height:366px}
.card-photo{width:100%;height:201px}
.card-body{height:165px;text-align:center;padding-top:16px;color:var(--white)}
.card-date{font-size:13px;font-weight:300;margin-bottom:10px}
.card-title{font-size:14px;letter-spacing:.3px;margin-bottom:10px}
.card-text{font-size:12px;font-weight:700;line-height:21px;padding:0 28px}
.card-more{font-size:13px;margin-top:12px;display:inline-flex;align-items:center;gap:8px}
.card-more .tri{border-left-color:currentColor}
.card-light .card-body{background:var(--panel);color:var(--ink);height:163px}
.card-light .card-more .tri{border-left-color:var(--green)}

/* map & address */
.map{left:0;top:1797px;width:1200px;height:478px;
  background:linear-gradient(120deg,#dfe9cf 0%,#e8eedd 40%,#cfe3f2 55%,#9fc8ec 62%,#e5ecd8 75%,#dbe7c9 100%)}
.address-box{left:763px;top:1945px;width:340px;height:330px;background:var(--address);color:var(--white);padding:30px 32px}
.address-box h4{font-size:18px;font-weight:400;margin-bottom:14px}
.address-row{display:flex;gap:14px;font-size:14px;font-weight:700;line-height:34px}
.address-row svg{flex:none;margin-top:11px}

/* footer */
.footer-nav{left:0;width:1200px;top:2310px;display:flex;justify-content:center;gap:36px;font-size:15px;color:#444}
.social{left:0;width:1200px;top:2373px;display:flex;justify-content:center;gap:44px}
.social span{width:18px;height:18px;border-radius:50%;background:#333}
.copyright{left:0;width:1200px;top:2418px;text-align:center;font-size:11px;color:#444;letter-spacing:.3px}
</style>
</head>
<body>

<header class="abs site-header">
  <div class="abs brand">
    <span class="brand-mark"></span>
    <span class="brand-name">RIDGEVIEW<small>LAWYERS</small></span>
  </div>
  <nav class="abs main-nav">
    <span>Home</span><span>Who we Are</span><span>Our Services</span><span>Articles</span><span>Terms &amp; Conditions</span><span>Contact us</span>
  </nav>
  <svg class="abs search-icon" width="16" height="16" viewBox="0 0 16 16"><circle cx="6.5" cy="6.5" r="5" fill="none" stroke="#444" stroke-width="2"/><line x1="10" y1="10" x2="15" y2="15" stroke="#444" stroke-width="2.4"/></svg>
</header>

<section class="abs hero" role="img" aria-label="City skyline at dusk with lit towers and a river bridge">
  <h1 class="abs hero-title">WELCOME TO RIDGEVIEW</h1>
  <div class="abs hero-sub"><span class="rule"></span>LAWYERS<span class="rule"></span></div>
  <p class="abs hero-text">Lorem ipsum dolor sit amet, consectetur adipiscing elit, sed do eiusmod tempor incididunt ut labore et dolore magna aliqua. Ut enim</p>
  <div class="abs hero-btn">READ MORE</div>
  <svg class="abs hero-arrow" style="left:128px" width="22" height="44" viewBox="0 0 22 44"><polyline points="20,2 2,22 20,42" fill="none" stroke="#fff" stroke-width="1.5"/></svg>
  <svg class="abs hero-arrow" style="left:1050px" width="22" height="44" viewBox="0 0 22 44"><polyline points="2,2 20,22 2,42" fill="none" stroke="#fff" stroke-width="1.5"/></svg>
</section>

<article class="abs panel panel-about">
  <h2>ABOUT US</h2>
  <p>Lorem ipsum dolor sit amet, consectetur adipiscing elit, sed do eiusmod tempor incididunt ut labore et dolore magna aliqua. Ut enim ad minim veniam, quis nostrud exercitation ullamco laboris nisi ut aliquip ex ea commodo consequat. Duis aute irure dolor in reprehenderit in voluptate velit esse cillum dolore eu fugiat nulla pariatur.</p>
  <span class="outline-btn">READ MORE</span>
</article>

<article class="abs panel panel-news">
  <h2>LATEST NEWS</h2>
  <p class="news-date">DATE : 08-DEC-2017</p>
  <p class="news-headline">Lorem ipsum dolor sit amet, consectetur adipiscing elit,</p>
  <p>sed do eiusmod tempor incididunt ut labore et dolore magna aliqua. Ut enim ad minim veniam, quis nostrud exercitation ullamco laboris nisi ut aliquip ex ea commodo consequat.</p>
  <span class="outline-btn">READ MORE</span>
</article>

<h2 class="abs features-title">EXCEPTEUR SINT OCCAECAT CUPIDATAT<br>NON PROIDENT,SUNT IN CULPA QU</h2>
<p class="abs features-intro">Lorem ipsum dolor sit amet, consectetur adipiscing elit, sed do eiusmod tempor incididunt ut labore et dolore magna aliqua. Ut enim ad minim veniam, quis nostrud exercitation ullamco laboris nisi ut aliquip ex ea commodo consequat. Duis aute irure dolor in reprehenderit in voluptate velit esse cillum dolore eu fugiat nulla pariatur.</p>

<div class="abs feature" style="left:171px">
  <h3>Who we are</h3>
  <p>Sed ut perspiciatis unde omnis iste natus error sit voluptatem accusantium doloremque laudantium, totam rem aperiam, eaque ipsa.</p>
  <span class="small-btn">Read More <i class="tri"></i></span>
</div>
<div class="abs feature" style="left:460px">
  <h3>What we do</h3>
  <p>Sed ut perspiciatis unde omnis iste natus error sit voluptatem accusantium doloremque laudantium, totam rem aperiam, eaque ipsa.</p>
  <span class="small-btn">Read More <i class="tri"></i></span>
</div>
<div class="abs feature" style="left:750px">
  <h3>Terms &amp; Conditions</h3>
  <p>Sed ut perspiciatis unde omnis iste natus error sit voluptatem accusantium doloremque laudantium, totam rem aperiam, eaque ipsa.</p>
  <span class="small-btn">Read More <i class="tri"></i></span>
</div>

<h2 class="abs articles-title">LATEST ARTICLES</h2>

<article class="abs card" style="left:118px">
  <div class="card-photo" role="img" aria-label="Two professionals meeting at an office desk" style="background:linear-gradient(135deg,#6b5a4a,#c9b79e 55%,#2c2c2e)"></div>
  <div class="card-body" style="background:var(--green)">
    <p class="card-date">14-DEC-2017</p>
    <p class="card-title">DUIS AUTE IRURE</p>
    <p class="card-text">Neque porro quisquam est, qui dolorem ipsum quia dolor sit amet, consectetur.</p>
    <span class="card-more">Read More <i class="tri"></i></span>
  </div>
</article>

<article class="abs card card-light" style="left:450px">
  <div class="card-body">
    <p class="card-date">14-DEC-2017</p>
    <p class="card-title">DUIS AUTE IRURE</p>
    <p class="card-text">Neque porro quisquam est, qui dolorem ipsum quia dolor sit amet, consectetur.</p>
    <span class="card-more">Read More <i class="tri"></i></span>
  </div>
  <div class="card-photo" role="img" aria-label="Businessman in a suit standing by office windows" style="height:203px;background:linear-gradient(90deg,#8a4a36,#c9d3dc 45%,#e7ecef 70%,#9aa6b2)"></div>
</article>

<article class="abs card" style="left:780px">
  <div class="card-photo" role="img" aria-label="Harbour city skyline with an opera house on the water" style="background:linear-gradient(180deg,#7fa9d4,#b9cfe4 45%,#2e5f8a 100%)"></div>
  <div class="card-body" style="background:var(--teal);height:165px">
    <p class="card-date">14-DEC-2017</p>
    <p class="card-title">DUIS AUTE IRURE</p>
    <p class="card-text">Neque porro quisquam est, qui dolorem ipsum quia dolor sit amet, consectetur.</p>
    <span class="card-more">Read More <i class="tri"></i></span>
  </div>
</article>

<section class="abs map" role="img" aria-label="Location map of the city region and bay"></section>

<aside class="abs address-box">
  <h4>Address</h4>
  <div class="address-row">
    <svg width="12" height="16" viewBox="0 0 12 16"><path d="M6 0a6 6 0 0 0-6 6c0 4.5 6 10 6 10s6-5.5 6-10A6 6 0 0 0 6 0z" fill="#fff"/><circle cx="6" cy="6" r="2.2" fill="#12a98f"/></svg>
    <span>Companyname, Eastbrook, 1st block<br>1234 Building no 8, floor 3</span>
  </div>
  <div class="address-row" style="margin-top:24px">
    <svg width="14" height="11" viewBox="0 0 14 11"><rect x=".7" y=".7" width="12.6" height="9.6" fill="none" stroke="#fff" stroke-width="1.4"/><polyline points="1,1 7,6 13,1" fill="none" stroke="#fff" stroke-width="1.4"/></svg>
    <span>Email:&nbsp; info@ridgeviewlaw.example</span>
  </div>
  <div class="address-row">
    <svg width="14" height="14" viewBox="0 0 14 14"><path d="M3 0l2.5 3.5-1.5 2c1 2 2.5 3.5 4.5 4.5l2-1.5L14 11l-2 3C6 13.5.5 8 0 2z" fill="#fff"/></svg>
    <span>Phone: 1-800 555 0142</span>
  </div>
</aside>

<footer>
  <nav class="abs footer-nav">
    <span>Home</span><span>Who we Are</span><span>Our Services</span><span>Articles</span><span>Terms &amp; Conditions</span><span>Contact us</span>
  </nav>
  <div class="abs social" aria-label="Social links">
    <span></span><span></span><span></span><span></span>
  </div>
  <p class="abs copyright">Copyrights © 2017 - All Rights Reserved</p>
</footer>

</body>
</html>
```